Criação de Papelaria para Brisa & Aurora
" Clinica Multidiciplinar com equipamentos de alta tecnologia para tratamentos esteticos faciais e corporais "

```html
<!DOCTYPE html>
<html lang="pt-BR">
<head>
<meta charset="UTF-8">
<title>Brisa &amp; Aurora — Papelaria</title>
<link rel="stylesheet" href="https://fonts.googleapis.com/css2?family=Josefin+Sans:wght@300;400&display=swap">
<style>
  :root {
    --backdrop: #626262;
    --cover-dark: #575757;
    --cover-light: #ececec;
    --ink-light: #f2f2f2;
    --ink-dark: #5a5a5a;
    --wire: #c9c9c9;
  }
  * { margin: 0; padding: 0; box-sizing: border-box; }
  html, body { width: 1200px; height: 1200px; overflow: hidden; }
  body {
    background: var(--backdrop);
    position: relative;
    font-family: "Josefin Sans", sans-serif;
  }
  .notepad { position: absolute; }
  .notepad__binding {
    position: absolute;
    left: 0; top: -28px;
    width: 100%; height: 56px;
  }
  .notepad__cover {
    position: absolute;
    inset: 0;
    overflow: hidden;
  }
  .notepad--light { left: 125px; top: 228px; width: 385px; height: 587px; }
  .notepad--light .notepad__cover { background: var(--cover-light); }
  .notepad--back { left: 696px; top: 228px; width: 384px; height: 572px; }
  .notepad--back .notepad__cover { background: var(--cover-dark); }
  .notepad--front { left: 390px; top: 444px; width: 385px; height: 552px; }
  .notepad--front .notepad__cover { background: var(--cover-dark); }

  .brand-name {
    position: absolute;
    left: 0; right: 0;
    text-align: center;
    font-weight: 300;
    text-transform: uppercase;
    white-space: nowrap;
  }
  .notepad--light .brand-name {
    top: 82px;
    font-size: 19px;
    letter-spacing: 2px;
    color: var(--ink-dark);
  }
  .notepad--front .brand-name {
    top: 240px;
    font-size: 29px;
    letter-spacing: 2.5px;
    color: var(--ink-light);
  }
  .contact {
    position: absolute;
    top: 508px;
    font-size: 8px;
    line-height: 13px;
    color: var(--ink-light);
    font-weight: 400;
    white-space: nowrap;
  }
  .contact--online { left: 84px; }
  .contact--address { left: 212px; }
</style>
</head>
<body>

  <div class="notepad notepad--light">
    <div class="notepad__cover">
      <p class="brand-name">Brisa &amp; Aurora</p>
    </div>
    <svg class="notepad__binding" viewBox="0 0 385 56" aria-hidden="true">
      <g fill="none" stroke="var(--wire)" stroke-width="3">
        <path d="M34 40 V18 a6 6 0 0 1 12 0 V40"/><path d="M59 40 V18 a6 6 0 0 1 12 0 V40"/>
        <path d="M84 40 V18 a6 6 0 0 1 12 0 V40"/><path d="M109 40 V18 a6 6 0 0 1 12 0 V40"/>
        <path d="M134 40 V18 a6 6 0 0 1 12 0 V40"/><path d="M159 40 V18 a6 6 0 0 1 12 0 V40"/>
        <path d="M184 40 V18 a6 6 0 0 1 12 0 V40"/><path d="M209 40 V18 a6 6 0 0 1 12 0 V40"/>
        <path d="M234 40 V18 a6 6 0 0 1 12 0 V40"/><path d="M259 40 V18 a6 6 0 0 1 12 0 V40"/>
        <path d="M284 40 V18 a6 6 0 0 1 12 0 V40"/><path d="M309 40 V18 a6 6 0 0 1 12 0 V40"/>
        <path d="M334 40 V18 a6 6 0 0 1 12 0 V40"/>
      </g>
    </svg>
  </div>

  <div class="notepad notepad--back">
    <div class="notepad__cover">
      <p class="contact contact--online">(21) 0000-0000<br>contato@brisaaurora.com.br<br>brisaaurora.com.br</p>
      <p class="contact contact--address">Avenida das Palmeiras, 120<br>Loja 04 - Centro<br>Rio de Janeiro - 20000-000</p>
    </div>
    <svg class="notepad__binding" viewBox="0 0 384 56" aria-hidden="true">
      <g fill="none" stroke="var(--wire)" stroke-width="3">
        <path d="M34 40 V18 a6 6 0 0 1 12 0 V40"/><path d="M59 40 V18 a6 6 0 0 1 12 0 V40"/>
        <path d="M84 40 V18 a6 6 0 0 1 12 0 V40"/><path d="M109 40 V18 a6 6 0 0 1 12 0 V40"/>
        <path d="M134 40 V18 a6 6 0 0 1 12 0 V40"/><path d="M159 40 V18 a6 6 0 0 1 12 0 V40"/>
        <path d="M184 40 V18 a6 6 0 0 1 12 0 V40"/><path d="M209 40 V18 a6 6 0 0 1 12 0 V40"/>
        <path d="M234 40 V18 a6 6 0 0 1 12 0 V40"/><path d="M259 40 V18 a6 6 0 0 1 12 0 V40"/>
        <path d="M284 40 V18 a6 6 0 0 1 12 0 V40"/><path d="M309 40 V18 a6 6 0 0 1 12 0 V40"/>
        <path d="M334 40 V18 a6 6 0 0 1 12 0 V40"/>
      </g>
    </svg>
  </div>

  <div class="notepad notepad--front">
    <div class="notepad__cover">
      <p class="brand-name">Brisa &amp; Aurora</p>
    </div>
    <svg class="notepad__binding" viewBox="0 0 385 56" aria-hidden="true">
      <g fill="none" stroke="var(--wire)" stroke-width="3">
        <path d="M34 40 V18 a6 6 0 0 1 12 0 V40"/><path d="M59 40 V18 a6 6 0 0 1 12 0 V40"/>
        <path d="M84 40 V18 a6 6 0 0 1 12 0 V40"/><path d="M109 40 V18 a6 6 0 0 1 12 0 V40"/>
        <path d="M134 40 V18 a6 6 0 0 1 12 0 V40"/><path d="M159 40 V18 a6 6 0 0 1 12 0 V40"/>
        <path d="M184 40 V18 a6 6 0 0 1 12 0 V40"/><path d="M209 40 V18 a6 6 0 0 1 12 0 V40"/>
        <path d="M234 40 V18 a6 6 0 0 1 12 0 V40"/><path d="M259 40 V18 a6 6 0 0 1 12 0 V40"/>
        <path d="M284 40 V18 a6 6 0 0 1 12 0 V40"/><path d="M309 40 V18 a6 6 0 0 1 12 0 V40"/>
        <path d="M334 40 V18 a6 6 0 0 1 12 0 V40"/>
      </g>
    </svg>
  </div>

</body>
</html>
```